VORN - Business cards

Business card to be created for Commercial sales staff

Target Market(s)

Commercial businesses

Industry/Entity Type

Commercial

Contact Information for Business Card

Look professional. For commercial clients

Colors
ffffff

Requirements
Must have
• - Vorn Logo
• - Commercial sales staff as postion
• - room for commerical sales manager role
• - person name and their mobile number
• - Website : vornelectrical.com.au
Nice to have
• White background.
• On back of business card just have the logo no other information
Should not have
• Should only have white background on front of card.

```html
<!DOCTYPE html>
<html lang="en">
<head>
<meta charset="utf-8">
<title>VORN – Business cards</title>
<link rel="stylesheet" href="https://fonts.googleapis.com/css2?family=Lato:wght@400;700;900&display=swap">
<style>
  :root {
    --stage: #545454;
    --stage-dark: #3f3f3f;
    --brand-red: #c20c14;
    --card-white: #ffffff;
    --logo-ink: #2e3138;
    --mark-tint: #f6dede;
    --soft-grey: #e2e2e2;
  }
  * { margin: 0; padding: 0; box-sizing: border-box; }
  html, body {
    width: 1200px;
    height: 900px;
    overflow: hidden;
  }
  body {
    background: linear-gradient(180deg, var(--stage) 0%, var(--stage-dark) 100%);
    font-family: "Lato", sans-serif;
    position: relative;
  }
  .card {
    position: absolute;
    top: 184px;
    height: 490px;
    box-shadow: 0 2px 6px rgba(0,0,0,0.25);
    overflow: hidden;
  }
  .card-front {
    left: 299px;
    width: 301px;
    background: var(--card-white);
    border-radius: 0 0 10px 10px;
  }
  .front-art {
    position: absolute;
    top: 0;
    left: 0;
  }
  .contact-block {
    position: absolute;
    left: 27px;
  }
  .person {
    top: 284px;
  }
  .person-name {
    font-size: 24px;
    font-weight: 400;
    line-height: 1.2;
    color: var(--brand-red);
  }
  .person-role {
    font-size: 19px;
    font-weight: 400;
    line-height: 1.3;
    color: var(--logo-ink);
  }
  .details {
    top: 378px;
    list-style: none;
    font-size: 17px;
    line-height: 25px;
    color: var(--logo-ink);
  }
  .card-back {
    left: 645px;
    width: 305px;
    border-radius: 12px;
    background: radial-gradient(ellipse 55% 45% at 50% 45%, var(--soft-grey) 0%, var(--card-white) 100%);
  }
  .brand-lockup {
    position: absolute;
    left: 50%;
    top: 50%;
    transform: translate(-50%, -50%) rotate(-90deg);
    display: flex;
    align-items: center;
    gap: 16px;
    white-space: nowrap;
  }
  .brand-dot {
    width: 44px;
    height: 44px;
    border-radius: 50%;
    background: var(--brand-red);
  }
  .brand-name {
    font-family: "Lato", sans-serif;
    font-weight: 900;
    font-size: 118px;
    line-height: 1;
    letter-spacing: 2px;
    color: var(--logo-ink);
  }
</style>
</head>
<body>
  <section class="card card-front" aria-label="Business card front">
    <svg class="front-art" width="301" height="260" viewBox="0 0 301 260">
      <path d="M301 92 C280 150 230 254 141 254 C80 254 30 228 0 186" fill="none" stroke="var(--brand-red)" stroke-width="4"/>
      <circle cx="141" cy="118" r="126" fill="var(--mark-tint)" role="img" aria-label="Brand mascot illustration area"/>
    </svg>
    <div class="contact-block person">
      <p class="person-name">Clara Whitfield</p>
      <p class="person-role">Commercial Sales Manager</p>
    </div>
    <ul class="contact-block details">
      <li>M: + 61 400111222</li>
      <li>E: hello@vornmail.com</li>
      <li>www.vornelectrical.com.au</li>
    </ul>
  </section>

  <section class="card card-back" aria-label="Business card back">
    <div class="brand-lockup">
      <span class="brand-dot"></span>
      <span class="brand-name">VORN</span>
    </div>
  </section>
</body>
</html>
```